Building Company Business Card Design

I am looking to get a business card designed for my Building Company. Please find the logo attached.

Industry/Entity Type

Business

Contact Information for Business Card

Mobile 0472 913 706
Email admin@harbourlineconstruct.com.au
Website www.harbourlineconstruct.com.au

Colors
0255a3

```html
<!DOCTYPE html>
<html lang="en">
<head>
<meta charset="utf-8">
<title>Harbourline Construct – Business Card</title>
<link rel="stylesheet" href="https://fonts.googleapis.com/css2?family=Arimo:wght@400;700&display=swap">
<style>
  :root {
    --brand-blue: #0255a3;
    --ink: #1a1a1a;
    --steel-grey: #6d6e70;
    --card-edge: #3a3a3a;
    --paper: #ffffff;
  }
  * { margin: 0; padding: 0; box-sizing: border-box; }
  html, body {
    width: 1200px;
    height: 450px;
    overflow: hidden;
    background: var(--paper);
    font-family: "Arimo", Arial, sans-serif;
  }
  .sheet {
    position: relative;
    width: 1200px;
    height: 450px;
  }
  .card {
    position: absolute;
    top: 70px;
    width: 515px;
    height: 315px;
    border: 1px solid var(--card-edge);
    background: var(--paper);
    overflow: hidden;
  }
  .card--front { left: 66px; }
  .card--back { left: 624px; }

  .skyline {
    position: absolute;
    left: 0;
    width: 100%;
  }
  .card--front .skyline {
    top: 18px;
    height: 72px;
    background: linear-gradient(180deg, rgba(2,85,163,0.55) 0%, var(--brand-blue) 55%, var(--brand-blue) 100%);
  }
  .card--back .skyline {
    bottom: 0;
    height: 72px;
    background: linear-gradient(180deg, rgba(109,110,112,0.5) 0%, var(--steel-grey) 55%, var(--steel-grey) 100%);
  }

  .holder {
    position: absolute;
    top: 126px;
    width: 100%;
    text-align: center;
  }
  .holder__name {
    color: var(--brand-blue);
    font-size: 24px;
    font-weight: 400;
    letter-spacing: 0.3px;
    line-height: 28px;
  }
  .holder__role {
    color: var(--ink);
    font-size: 21px;
    font-weight: 400;
    line-height: 28px;
  }

  .contacts {
    position: absolute;
    top: 210px;
    left: 74px;
    list-style: none;
  }
  .contacts__item {
    display: flex;
    align-items: center;
    height: 27.5px;
    color: var(--ink);
    font-size: 16.5px;
  }
  .contacts__icon {
    width: 16px;
    height: 16px;
    margin-right: 11px;
    flex: none;
  }
  .contacts__value--phone { font-size: 19px; margin-left: 5px; }
  .contacts__label + .contacts__value { margin-left: 5px; }

  .brand {
    position: absolute;
    top: 112px;
    width: 100%;
    display: flex;
    justify-content: center;
    align-items: center;
    gap: 12px;
  }
  .brand__dot {
    width: 16px;
    height: 16px;
    border-radius: 50%;
    background: var(--brand-blue);
  }
  .brand__name {
    color: var(--brand-blue);
    font-size: 31px;
    font-weight: 700;
    letter-spacing: 0.5px;
  }
</style>
</head>
<body>
<main class="sheet">

  <section class="card card--front">
    <div class="skyline" role="img" aria-label="Blue city skyline illustration of office towers"></div>

    <div class="holder">
      <p class="holder__name">DARA QUYNH. NGUYEN</p>
      <p class="holder__role">General Director</p>
    </div>

    <ul class="contacts">
      <li class="contacts__item">
        <svg class="contacts__icon" viewBox="0 0 24 24" aria-hidden="true">
          <path fill="#0255a3" d="M6.6 10.8a15.1 15.1 0 0 0 6.6 6.6l2.2-2.2a1 1 0 0 1 1-.25 11.4 11.4 0 0 0 3.6.57 1 1 0 0 1 1 1V20a1 1 0 0 1-1 1A17 17 0 0 1 3 4a1 1 0 0 1 1-1h3.5a1 1 0 0 1 1 1c0 1.25.2 2.45.57 3.57a1 1 0 0 1-.25 1z"/>
        </svg>
        <span class="contacts__label">Mobile:</span><span class="contacts__value contacts__value--phone">0472 913 706</span>
      </li>
      <li class="contacts__item">
        <svg class="contacts__icon" viewBox="0 0 24 24" aria-hidden="true">
          <circle cx="12" cy="12" r="4" fill="none" stroke="#0255a3" stroke-width="3"/>
          <path d="M16 8v5.5a2.5 2.5 0 0 0 5 0V12a9 9 0 1 0-3.5 7.1" fill="none" stroke="#0255a3" stroke-width="3" stroke-linecap="round"/>
        </svg>
        <span class="contacts__label">Email:</span><span class="contacts__value">admin@harbourlineconstruct.com.au</span>
      </li>
      <li class="contacts__item">
        <svg class="contacts__icon" viewBox="0 0 24 24" aria-hidden="true">
          <circle cx="12" cy="12" r="10" fill="#0255a3"/>
          <path d="M2 12h20M12 2c3 3 3 17 0 20M12 2c-3 3-3 17 0 20" fill="none" stroke="#fff" stroke-width="1.6"/>
        </svg>
        <span class="contacts__label">Website:</span><span class="contacts__value">www.harbourlineconstruct.com.au</span>
      </li>
    </ul>
  </section>

  <section class="card card--back">
    <div class="brand">
      <span class="brand__dot" aria-hidden="true"></span>
      <span class="brand__name">HARBOURLINE CONSTRUCT</span>
    </div>
    <div class="skyline" role="img" aria-label="Grey city skyline illustration of office towers"></div>
  </section>

</main>
</body>
</html>
```